Thank You Card design for a federal credit union

I am looking to have a thank you card designed.
Specs:
Flat size of 9.5"x6.5" folds to final size of 4.75"x6.5", it will print full color on the front and back. Below, you will see their logo, which needs to print on the inside of the folded card. I also attached images of their current card. They would like to keep the blue color but are open to design on the front. This is a Federal Credit Union, so please make the design, modern and professional. Below is the text that needs to print below the logo on the inside of the card. The text and logo will print below the fold on the inside, leave the top portion (above the panel) white.
Inside text:
Our Members are the foundation of our Credit Union. We sincerely thank you for your loyalty, your business and the opportunity to serve you.
Target Market(s)
Clients of a federal credit union
Industry/Entity Type
Union
Requirements
Must have
- a simple, professional, and modern feel. "Thank You for your business" must be on the front section in some variation.
Should not have
- nothing flashy or too many colors. keep it simple

```html
<!DOCTYPE html>
<html lang="en">
<head>
<meta charset="utf-8">
<title>Thank You Card – Outside Panels</title>
<link rel="stylesheet" href="https://fonts.googleapis.com/css2?family=Michroma&family=Parisienne&family=Arimo:wght@400;700&family=Tinos:ital@1&display=swap">
<style>
  :root {
    --board: #e9e6df;
    --label: #111111;
    --card-edge: #1b2169;
    --card-glow: #1467a6;
    --card-mid: #1d3f8c;
    --ink-light: #ffffff;
  }
  * { margin: 0; padding: 0; box-sizing: border-box; }
  html, body { width: 1200px; height: 1146px; overflow: hidden; }
  body {
    position: relative;
    background: var(--board);
    font-family: "Arimo", Arial, sans-serif;
  }
  .board-label {
    position: absolute;
    font-size: 14px;
    color: var(--label);
    white-space: nowrap;
  }
  .label-front { left: 150px; top: 62px; }
  .label-front-size { left: 998px; top: 390px; }
  .label-outside { left: 30px; top: 575px; }
  .label-back-size { left: 998px; top: 960px; }
  .label-back { left: 153px; top: 1070px; }

  .card-panel {
    position: absolute;
    left: 240px;
    width: 701px;
    height: 513px;
    overflow: hidden;
  }
  .card-front {
    top: 50px;
    background: radial-gradient(ellipse 62% 70% at 50% 55%, var(--card-glow) 0%, var(--card-mid) 48%, var(--card-edge) 85%);
  }
  .card-back {
    top: 599px;
    background: radial-gradient(ellipse 60% 68% at 51% 47%, var(--card-glow) 0%, var(--card-mid) 48%, var(--card-edge) 85%);
  }

  .front-intro, .front-closing {
    position: absolute;
    font-family: "Michroma", "Arial Black", sans-serif;
    color: var(--ink-light);
    transform: skewX(-14deg);
    white-space: nowrap;
    text-shadow: 1px 1px 2px rgba(0, 0, 0, 0.45);
  }
  .front-intro {
    left: 86px;
    top: 154px;
    font-size: 21px;
    letter-spacing: 4px;
  }
  .front-thanks {
    position: absolute;
    left: 176px;
    top: 236px;
    font-family: "Parisienne", cursive;
    font-size: 88px;
    line-height: 1;
    letter-spacing: 8px;
    color: var(--ink-light);
    white-space: nowrap;
    text-shadow: 2px 3px 3px rgba(0, 0, 0, 0.5);
  }
  .front-closing {
    right: 50px;
    top: 320px;
    font-size: 20px;
    line-height: 28px;
    letter-spacing: 4px;
    text-align: right;
  }

  .back-brand {
    position: absolute;
    left: 40px;
    bottom: 16px;
    color: var(--ink-light);
  }
  .brand-tagline {
    display: block;
    font-family: "Tinos", Georgia, serif;
    font-style: italic;
    font-size: 12px;
    margin-left: 8px;
    margin-bottom: 4px;
  }
  .brand-name {
    display: block;
    font-family: "Michroma", "Arial Black", sans-serif;
    font-size: 20px;
    line-height: 30px;
    letter-spacing: 0;
  }
  .brand-sub {
    display: block;
    font-family: "Michroma", "Arial Black", sans-serif;
    font-size: 6px;
    letter-spacing: 0.6px;
    margin-top: 2px;
  }
  .back-punch {
    position: absolute;
    left: 340px;
    top: 464px;
  }
</style>
</head>
<body>
  <span class="board-label label-front">Front Part</span>
  <span class="board-label label-front-size">size of 4.75"x6.5"</span>
  <span class="board-label label-outside">outside of the folded card</span>
  <span class="board-label label-back-size">size of 4.75"x6.5"</span>
  <span class="board-label label-back">Back part</span>

  <section class="card-panel card-front">
    <p class="front-intro">WE WOULD LIKE TO SAY</p>
    <p class="front-thanks">thank you...</p>
    <p class="front-closing">STAY<br>WITH US</p>
  </section>

  <section class="card-panel card-back">
    <div class="back-brand">
      <span class="brand-tagline">"people over profit"</span>
      <span class="brand-name">Harborline</span>
      <span class="brand-sub">FEDERAL CREDIT UNION</span>
    </div>
    <svg class="back-punch" width="34" height="34" viewBox="0 0 34 34" aria-hidden="true">
      <circle cx="17" cy="17" r="17" fill="#ffffff"/>
    </svg>
  </section>
</body>
</html>
```